Interior Decorating business - Logo & Stationery

"Velmora Spaces" is a newly established interior decorating company, based in Sydney, providing interior decorating, colour consulting and property styling services to residential and commercial clients.

We require a logo and stationery design (double-sided business card, A4 letterhead and with compliments slip (210mm X 95mm))

Letterhead information and with compliments slip:
Address - 9/31-33 Tindale Rd, Garrow Point NSW 2047
Phone - (02)9617 4082
Mobile - 0428 305 961
Email - nadia@velmoraspaces.com.au
Web - www.velmoraspaces.com.au
ABN - 47839205164

Business Cards should be double sided and are to include;
Nadia Kowal
Director

with email address, mobile number, website as listed above

They also need to include services offered i.e. Interior Decorating, Colour Consulting, Property Styling

Please note that the current content on the website will be updated, so disregard logo and content currently on the website.

Target Market(s)

Target market is two-fold - residential clients (primarily homeowners with pride in their homes) and commerical clients (specifically business owners of retail shops and cafes and property developers)

Industry/Entity Type

Residential

```html
<!DOCTYPE html>
<html lang="en">
<head>
<meta charset="utf-8">
<title>Velmora Spaces – Logo &amp; Stationery</title>
<link rel="stylesheet" href="https://fonts.googleapis.com/css2?family=Arimo:wght@400;700&family=Tinos:ital@0;1&display=swap">
<style>
  :root {
    --maroon: #5b1a35;
    --pink: #d99bb2;
    --pink-soft: #f0cdd9;
    --mauve: #b9718e;
    --paper: #ffffff;
    --edge: #d8d8d8;
    --ink: #3a1425;
  }
  * { box-sizing: border-box; margin: 0; padding: 0; }
  html, body { width: 1200px; height: 900px; overflow: hidden; background: var(--paper); }
  body { position: relative; font-family: "Arimo", Arial, sans-serif; color: var(--ink); }

  .brand { position: absolute; display: flex; align-items: center; gap: 10px; }
  .brand__dot { border-radius: 50%; background: var(--pink); flex: none; }
  .brand__name { font-family: "Tinos", "Times New Roman", serif; font-weight: 400; color: var(--maroon); white-space: nowrap; line-height: 1; }
  .brand--light .brand__name { color: var(--paper); }

  .sheet { position: absolute; background: var(--paper); border: 1px solid var(--edge); box-shadow: 2px 3px 8px rgba(0,0,0,.18); overflow: hidden; }

  .contact { position: absolute; font-weight: 700; font-size: 11px; line-height: 14px; color: var(--ink); }
  .phones { position: absolute; font-size: 9px; line-height: 12px; color: var(--ink); }

  .services { position: absolute; display: flex; gap: 22px; font-weight: 700; font-size: 12px; color: var(--ink); white-space: nowrap; }
  .services span + span::before { content: "|"; margin-right: 22px; font-weight: 400; }

  .deco { position: absolute; border-radius: 50%; background: radial-gradient(circle at 40% 40%, var(--pink-soft), var(--pink)); opacity: .75; }

  /* Main logo */
  .hero-logo { left: 80px; top: 48px; flex-direction: column; align-items: flex-start; gap: 14px; }
  .hero-logo .brand__dot { width: 50px; height: 50px; margin-left: 40px; }
  .hero-logo .brand__name { font-size: 54px; }

  /* Letterhead */
  .letterhead { left: 34px; top: 194px; width: 548px; height: 686px; }
  .letterhead .contact { left: 16px; top: 12px; }
  .letterhead .brand { right: 16px; top: 18px; flex-direction: column; align-items: flex-end; gap: 6px; }
  .letterhead .brand__dot { width: 22px; height: 22px; }
  .letterhead .brand__name { font-size: 22px; }
  .letterhead__rule { position: absolute; left: 6px; right: 130px; top: 88px; height: 3px; background: var(--maroon); }
  .letterhead .phones { right: 16px; top: 96px; }
  .letterhead .deco { left: 18px; top: 500px; width: 140px; height: 140px; }
  .letterhead .services { left: 108px; top: 646px; }

  /* Dark card back */
  .card-back { left: 660px; top: 30px; width: 480px; height: 190px; background: var(--maroon); border: none; }
  .card-back .brand { left: 0; right: 0; top: 38px; flex-direction: column; gap: 14px; }
  .card-back .brand__dot { width: 40px; height: 40px; }
  .card-back .brand__name { font-size: 46px; }

  /* Business card front */
  .card-front { left: 660px; top: 310px; width: 490px; height: 226px; }
  .card-front .brand { left: 16px; top: 20px; flex-direction: column; align-items: flex-start; gap: 8px; }
  .card-front .brand__dot { width: 24px; height: 24px; margin-left: 22px; }
  .card-front .brand__name { font-size: 28px; }
  .person { position: absolute; right: 24px; top: 26px; font-family: "Tinos", "Times New Roman", serif; color: var(--maroon); text-align: center; }
  .person__name { font-size: 32px; line-height: 36px; }
  .person__role { font-size: 22px; line-height: 24px; text-align: right; margin-right: 8px; }
  .card-front .contact { left: 12px; top: 104px; }
  .card-front .phones { right: 14px; top: 148px; text-align: left; }
  .card-front .services { left: 12px; top: 176px; font-size: 11px; gap: 18px; }
  .card-front .services span + span::before { margin-right: 18px; }
  .card-front__band { position: absolute; left: 0; right: 0; bottom: 0; height: 20px; background: var(--maroon); color: var(--paper); font-size: 10px; line-height: 20px; letter-spacing: 16px; text-align: center; white-space: nowrap; }

  /* Compliments slip */
  .slip { left: 610px; top: 586px; width: 572px; height: 284px; }
  .slip .brand { left: 20px; top: 18px; flex-direction: column; align-items: flex-start; gap: 10px; }
  .slip .brand__dot { width: 40px; height: 40px; margin-left: 40px; }
  .slip .brand__name { font-size: 44px; }
  .slip .contact { left: 320px; top: 8px; }
  .slip__greeting { position: absolute; left: 38px; top: 138px; font-family: "Tinos", "Times New Roman", serif; font-style: italic; font-size: 34px; color: var(--maroon); }
  .slip .deco { right: 18px; top: 128px; width: 100px; height: 100px; }
  .slip .services { left: 8px; top: 252px; font-size: 11px; }
</style>
</head>
<body>

  <div class="brand hero-logo">
    <span class="brand__dot"></span>
    <span class="brand__name">Velmora Spaces</span>
  </div>

  <section class="sheet letterhead" aria-label="A4 letterhead">
    <p class="contact">Address - 9/31-33 Tindale Rd,<br>Garrow Point NSW 2047<br>Email - nadia@velmoraspaces.com.au<br>Web - www.velmoraspaces.com.au</p>
    <div class="brand">
      <span class="brand__dot"></span>
      <span class="brand__name">Velmora Spaces</span>
    </div>
    <div class="letterhead__rule"></div>
    <p class="phones">Phone - (02)9617 4082<br>Mobile - 0428 305 961</p>
    <div class="deco" role="img" aria-label="Soft pink brand accent"></div>
    <p class="services"><span>Interior Decorating</span><span>Colour Consulting</span><span>Property Styling</span></p>
  </section>

  <section class="sheet card-back" aria-label="Business card, back">
    <div class="brand brand--light">
      <span class="brand__dot"></span>
      <span class="brand__name">Velmora Spaces</span>
    </div>
  </section>

  <section class="sheet card-front" aria-label="Business card, front">
    <div class="brand">
      <span class="brand__dot"></span>
      <span class="brand__name">Velmora Spaces</span>
    </div>
    <div class="person">
      <p class="person__name">Nadia Kowal</p>
      <p class="person__role">Director</p>
    </div>
    <p class="contact">Address - 9/31-33 Tindale Rd,<br>Garrow Point NSW 2047<br>Email - nadia@velmoraspaces.com.au<br>Web - www.velmoraspaces.com.au</p>
    <p class="phones">Phone - (02)9617 4082<br>Mobile - 0428 305 961</p>
    <p class="services"><span>Interior Decorating</span><span>Colour Consulting</span><span>Property Styling</span></p>
    <p class="card-front__band">www.velmoraspaces.com</p>
  </section>

  <section class="sheet slip" aria-label="With compliments slip">
    <div class="brand">
      <span class="brand__dot"></span>
      <span class="brand__name">Velmora Spaces</span>
    </div>
    <p class="contact">Address - 9/31-33 Tindale Rd,<br>Garrow Point NSW 2047<br>Web - www.velmoraspaces.com.au<br>Phone - (02)9617 4082<br>Mobile - 0428 305 961</p>
    <p class="slip__greeting">With compliments....</p>
    <div class="deco" role="img" aria-label="Soft pink brand accent"></div>
    <p class="services"><span>Interior Decorating</span><span>Colour Consulting</span><span>Property Styling</span></p>
  </section>

</body>
</html>
```